Post card design for ( Interior ) & ( Exterior ) Residential Painting

We need a post card design for interior painting. To get homeowners to call about getting there interior home painted before the end winter comes, to get a clean, quality and no hassle paint job with low odor paints

Some IDEAS:
Exterior Paint Season is Coming to Northern VA and Metro DC!
Have you taken a look around your house this winter? Have you noticed any areas of unwanted moisture, mold or draft? Keeping your house painted and well-maintained on the outside will save money in the future as well. It protects your home from the elements – whether, wind, rain and snow or the strong summer sun.

idea #2
Exterior Paint Makes Your House Last Longer
aintaining a good coat of the correct type of paint on the exterior of your home will help protect your home from the elements and extend the overall life of the structure
idea #3
Rotten Wood and Two Other TOP Reasons for Exterior Paint
We’ll start there – rotten wood – the first reason for exterior paint. If your home or building has decorative wood trim, wood siding or even wood around windows and doors, it could be at risk for rotten or rotting wood. Maintaining a healthy and COMPLETE coat of paint will protect the wood from water damage. Additionally, during a paint project, our team can assess wooden areas and advise if there are any places of concern. For a long-term solution, consider replacing wood trim with vinyl or wood alternatives that stand up to the elements. This can also be done during an exterior paint project.
Idea # 4
Benefits of Using Low-VOC interior Paints
Paints with low-VOC or Zero-VOC are considered healthier options due to the lower amount of toxins they release when applied to a wall. Latex paints are popular low-VOC because they are water based and don’t contain other chemicals you may find in oil-based paints.

Less odor! Because these paints have lower levels of toxins that are released, the paint smell that is associated with a fresh coat of paint is not as strong. Low-VOC would be a great option if you plan on painting a nursery because the smell won’t linger. Although you might not smell it, it is always important to ventilate the room. All paints, even low-VOC have levels of toxicity which are not good to breathe in for long periods of time.

Target Market(s)

single family homes

Colors

Designer to choose colors to be used in the design.

Requirements
Should not have
• cheep, free

```html
<!DOCTYPE html>
<html lang="en">
<head>
<meta charset="utf-8">
<title>Brightline Painting – Exterior Season Postcard</title>
<link href="https://fonts.googleapis.com/css2?family=Bebas+Neue&family=Open+Sans:ital,wght@0,400;0,600;0,700;0,800;1,800&display=swap" rel="stylesheet">
<style>
:root{
  --red:#e3151a;
  --red-dark:#b80f13;
  --ink:#1b1b1b;
  --black:#111;
  --paper:#ffffff;
  --panel:#f2f2f2;
  --grey:#6b6b6b;
  --bg:#e4e2df;
}
*{box-sizing:border-box;margin:0;padding:0}
html,body{width:1106px;height:1200px;overflow:hidden}
body{background:var(--bg);font-family:"Open Sans",Arial,sans-serif;color:var(--ink);position:relative}
.card{position:absolute;left:113px;width:880px;height:480px;background:var(--panel);overflow:hidden;box-shadow:0 6px 18px rgba(0,0,0,.25)}
.card--front{top:80px}
.card--back{top:640px;background:var(--paper)}
.layer{position:absolute;inset:0}
.wordmark{position:absolute;display:flex;align-items:center;gap:8px;font-weight:800;color:var(--ink);line-height:1}
.wordmark__dot{width:16px;height:16px;background:var(--red)}
.front-mark{left:22px;top:52px;font-size:26px}
.headline{position:absolute;left:220px;top:28px;font-weight:800;font-style:italic;font-size:17px;line-height:1.4;color:var(--red);text-transform:uppercase;white-space:nowrap}
.headline b{color:var(--ink);font-weight:800}
.question-band{position:absolute;left:0;top:145px;width:510px;height:70px;padding:10px 0 0 22px;color:#fff;font-weight:700;font-size:12.5px;line-height:25px;white-space:nowrap}
.tick{display:inline-block;width:12px;height:12px;border:1.5px solid #fff;margin-right:8px;vertical-align:-1px;position:relative}
.tick::after{content:"";position:absolute;left:3px;top:0;width:4px;height:7px;border:solid #fff;border-width:0 2px 2px 0;transform:rotate(40deg)}
.intro{position:absolute;left:20px;top:230px;width:385px;font-size:11px;line-height:1.4}
.services{position:absolute;left:20px;top:288px;list-style:none;font-size:11.2px;line-height:23.5px}
.services li::before{content:"";display:inline-block;width:13px;height:13px;border-radius:3px;background:var(--red);margin-right:10px;vertical-align:-2px}
.badge{position:absolute;width:126px;height:126px}
.badge__text{position:absolute;inset:0;display:flex;align-items:center;justify-content:center;text-align:center;color:#fff;font-weight:700;font-size:16px;line-height:1.2}
.badge--front{left:345px;top:280px}
.badge--back{left:400px;top:300px;width:112px;height:112px}
.badge--back .badge__text{font-size:14px}
.footer{position:absolute;left:0;bottom:0;width:100%;height:50px;background:var(--black);display:flex;align-items:center;font-size:13px;color:#fff}
.footer__phone{width:262px;height:50px;background:var(--red);clip-path:polygon(0 0,100% 0,94% 100%,0 100%);display:flex;align-items:center;padding-left:20px;font-size:29px;font-weight:600;letter-spacing:.5px}
.footer__tag{color:var(--red);font-weight:800;font-size:11px;margin-left:18px;text-transform:uppercase}
.footer__contact{margin-left:14px;font-weight:600}
.back-banner{position:absolute;left:0;top:160px;width:455px;height:56px;background:var(--red);clip-path:polygon(0 0,96% 0,100% 100%,0 100%);color:#fff;text-align:center;padding:7px 18px 0 0}
.back-banner h2{font-family:"Bebas Neue","Arial Narrow",sans-serif;font-weight:400;font-size:20px;line-height:1.1;letter-spacing:.2px;white-space:nowrap}
.back-banner p{font-weight:700;font-size:11.5px;margin-top:4px;white-space:nowrap}
.back-copy{position:absolute;left:20px;top:228px;width:368px;font-size:10.6px;line-height:1.42}
.back-copy p+p{margin-top:13px}
.tag{position:absolute;background:var(--red);color:#fff;font-weight:800;font-size:13px;padding:2px 18px;transform:rotate(-45deg);transform-origin:left top}
.divider{position:absolute;left:545px;top:135px;width:1px;height:295px;background:#9a9a9a}
.return{position:absolute;left:485px;top:25px;font-size:12.5px;font-weight:700;color:var(--grey);line-height:1.45;font-style:normal}
.return .wordmark{position:static;font-size:17px;margin-bottom:14px;color:var(--ink)}
.return .wordmark__dot{width:12px;height:12px}
.indicia{position:absolute;left:760px;top:28px;width:102px;padding:7px 0;border:1px solid #777;text-align:center;font-family:Arial,sans-serif;font-size:13px;line-height:1.25;color:#111}
.mail-box{position:absolute;left:570px;top:183px;width:285px;height:112px;border:1px solid #777;font-family:Arial,sans-serif;color:#111;background:var(--paper)}
.mail-box__route{position:absolute;right:20px;top:12px;font-size:11px}
.mail-box__to{position:absolute;left:20px;top:52px;font-size:16px;line-height:1.2}
</style>
</head>
<body>

<section class="card card--front" aria-label="Postcard front">
  <svg class="layer" viewBox="0 0 880 480" aria-hidden="true">
    <defs>
      <linearGradient id="houseTone" x1="0" y1="0" x2="0" y2="1">
        <stop offset="0" stop-color="#c9d5df"/>
        <stop offset=".45" stop-color="#7f93aa"/>
        <stop offset="1" stop-color="#8a8676"/>
      </linearGradient>
    </defs>
    <path d="M590 0 H880 V430 H382 Q510 200 590 0 Z" fill="url(#houseTone)" role="img" aria-label="Photo of a blue-grey two-storey house with white garage door"/>
    <path d="M580 0 Q500 200 372 430" fill="none" stroke="var(--black)" stroke-width="12"/>
    <circle cx="612" cy="368" r="38" fill="#b7b4ad" stroke="#fff" stroke-width="3" role="img" aria-label="Close-up of painted trim"/>
    <circle cx="680" cy="368" r="38" fill="#7a6a5c" stroke="#fff" stroke-width="3" role="img" aria-label="Close-up of brick and blue door"/>
    <circle cx="748" cy="368" r="38" fill="#9b9388" stroke="#fff" stroke-width="3" role="img" aria-label="Close-up of weathered wood"/>
    <path d="M0 145 H510 L496 215 H0 Z" fill="var(--red)"/>
  </svg>

  <div class="wordmark front-mark"><span class="wordmark__dot"></span>BRIGHTLINE<br>PAINTING</div>
  <h1 class="headline">Exterior paint season<br><b>is coming</b> to Northern<br>VA and Metro DC!</h1>

  <div class="question-band">
    <div><span class="tick"></span>Have you taken a look around your house this winter?</div>
    <div><span class="tick"></span>Have you noticed any areas of unwanted moisture, mold or draft?</div>
  </div>

  <p class="intro">Keeping your house painted and well-maintained on the outside will save money in the future as well. It protects your home from the elements – whether, wind, rain and snow or the strong summer sun.</p>

  <ul class="services">
    <li>Painting interior and exterior</li>
    <li>Exterior painters of wood, siding, stucco, brick</li>
    <li>Kitchen cabinet and molding facelifts</li>
    <li>Deck restoration, staining, painting, power washing</li>
    <li>Professional pre-painting prep – priming</li>
    <li>Wallpapering – removal service</li>
  </ul>

  <div class="badge badge--front">
    <svg viewBox="0 0 126 126" width="126" height="126" aria-hidden="true">
      <circle cx="63" cy="63" r="56" fill="none" stroke="var(--red)" stroke-width="10" stroke-dasharray="4.5 4.3"/>
      <circle cx="63" cy="63" r="55" fill="var(--red)"/>
      <circle cx="63" cy="63" r="49" fill="none" stroke="var(--red-dark)" stroke-width="1.5"/>
    </svg>
    <div class="badge__text">QUALITY &amp;<br>NO HASSLE<br>PAINT JOB</div>
  </div>

  <footer class="footer">
    <div class="footer__phone">555-014-2287</div>
    <span class="footer__tag">Locally owned and operated!</span>
    <span class="footer__contact">hello@brightlinepainting.com | www.brightlinepainting.com</span>
  </footer>
</section>

<section class="card card--back" aria-label="Postcard back">
  <svg class="layer" viewBox="0 0 880 480" aria-hidden="true">
    <path d="M0 0 H448 Q400 220 452 430 H0 Z" fill="var(--panel)"/>
    <rect x="0" y="0" width="197" height="160" fill="#c7c6c2" role="img" aria-label="Before photo: faded white house wall"/>
    <rect x="203" y="0" width="240" height="160" fill="#6f7f92" role="img" aria-label="After photo: freshly painted blue-grey wall"/>
    <path d="M456 0 Q406 220 460 430" fill="none" stroke="var(--black)" stroke-width="12"/>
  </svg>
  <span class="tag" style="left:2px;top:44px">BEFORE</span>
  <span class="tag" style="left:205px;top:44px">AFTER</span>

  <div class="back-banner">
    <h2>Exterior paint season is coming to Northern VA and Metro DC!</h2>
    <p>Rotten Wood and Two Other TOP Reasons for Exterior Paint</p>
  </div>

  <div class="back-copy">
    <p>We’ll start there – rotten wood – the first reason for exterior paint. If your home or building has decorative wood trim, wood siding or even wood around windows and doors, it could be at risk for rotten or rotting wood. Maintaining a healthy and COMPLETE coat of paint will protect the wood from water damage. Additionally, during a paint project, our team can assess wooden areas and advise if there are any places of concern.</p>
    <p>For a long-term solution, consider replacing wood trim with vinyl or wood alternatives that stand up to the elements. This can also be done during an exterior paint project.</p>
  </div>

  <div class="badge badge--back">
    <svg viewBox="0 0 126 126" width="112" height="112" aria-hidden="true">
      <circle cx="63" cy="63" r="56" fill="none" stroke="var(--red)" stroke-width="10" stroke-dasharray="4.5 4.3"/>
      <circle cx="63" cy="63" r="55" fill="var(--red)"/>
      <circle cx="63" cy="63" r="49" fill="none" stroke="var(--red-dark)" stroke-width="1.5"/>
    </svg>
    <div class="badge__text">QUALITY &amp;<br>NO HASSLE<br>PAINT JOB</div>
  </div>

  <div class="divider"></div>

  <address class="return">
    <div class="wordmark"><span class="wordmark__dot"></span>BRIGHTLINE<br>PAINTING</div>
    BRIGHTLINE PAINTING<br>418 Maple Hollow Road, Suite 3B<br>Cedar Grove, VA 22000
  </address>

  <div class="indicia">PRSRT STD<br>ECRWSS<br>U.S. Postage<br><b>PAID</b><br>EDDM RETAIL</div>

  <div class="mail-box">
    <span class="mail-box__route">*****************ECRWSS****</span>
    <div class="mail-box__to">Local<br>Postal Customer</div>
  </div>

  <footer class="footer">
    <div class="footer__phone">555-014-2287</div>
    <span class="footer__tag">Locally owned and operated!</span>
    <span class="footer__contact">hello@brightlinepainting.com | www.brightlinepainting.com</span>
  </footer>
</section>

</body>
</html>
```